Plakat-Design für Werbetafel-Design für Fussballplatz
Zielgruppe
IT Consulting Dienstleistungen für Internationale Kunden
Aufgabenstellung
Werbetafel-Design für Fussballplatz. (Logo in groß + Slogan 'THE NORVEK ADVISORS')
Format: 3,0 x 0,75 m
Druckdatenvorabe anbei.

```html
<!DOCTYPE html>
<html lang="en">
<head>
<meta charset="utf-8">
<title>KELDARON – Pitch Side Board</title>
<link href="https://fonts.googleapis.com/css2?family=Montserrat:wght@400&family=Raleway:wght@500&family=Lato:wght@300&display=swap" rel="stylesheet">
<style>
  :root {
    --brand-blue: #0694d4;
    --brand-green: #87a92a;
    --ink: #1a1a1a;
    --paper: #ffffff;
    --stage: #ffffff;
  }
  html, body {
    margin: 0;
    width: 1200px;
    height: 600px;
    overflow: hidden;
    background: var(--stage);
  }
  .board-wrap {
    position: absolute;
    left: 40px;
    top: 160px;
    width: 1120px;
    height: 280px;
  }
  .board {
    position: absolute;
    left: 0;
    top: 0;
    width: 1600px;
    height: 400px;
    transform: scale(0.7);
    transform-origin: 0 0;
    background: var(--paper);
    outline: 1.4px solid var(--ink);
    overflow: hidden;
  }
  .brand-dot {
    position: absolute;
    left: 120px;
    top: 72px;
    width: 150px;
    height: 150px;
    border-radius: 50%;
    background: var(--brand-blue);
  }
  .brand-name {
    position: absolute;
    left: 300px;
    top: 84px;
    margin: 0;
    font-family: "Montserrat", sans-serif;
    font-weight: 400;
    font-size: 104px;
    line-height: 1;
    letter-spacing: -1px;
    color: var(--ink);
  }
  .brand-tagline {
    position: absolute;
    right: 740px;
    top: 190px;
    margin: 0;
    font-family: "Raleway", sans-serif;
    font-weight: 500;
    font-size: 38px;
    line-height: 1;
    color: var(--brand-blue);
  }
  .accent-bar {
    position: absolute;
    left: 0;
    top: 307px;
    width: 475px;
    height: 44px;
    background: var(--brand-blue);
  }
  .slogan {
    position: absolute;
    left: 493px;
    top: 264px;
    height: 87px;
    margin: 0;
    padding: 0 20px;
    display: flex;
    align-items: center;
    background: var(--brand-green);
    font-family: "Lato", sans-serif;
    font-weight: 300;
    font-size: 76px;
    line-height: 1;
    letter-spacing: -0.5px;
    color: var(--paper);
    white-space: nowrap;
  }
  .corner-decoration {
    position: absolute;
    left: 1236px;
    top: 0;
    width: 364px;
    height: 230px;
    background: linear-gradient(225deg,
      rgba(6, 148, 212, 0.55) 0%,
      rgba(135, 169, 42, 0.40) 45%,
      rgba(255, 255, 255, 0) 85%);
  }
</style>
</head>
<body>
  <div class="board-wrap">
    <section class="board" aria-label="Pitch side advertising board">
      <div class="brand-dot"></div>
      <h1 class="brand-name">KELDARON</h1>
      <p class="brand-tagline">IT Consulting</p>
      <div class="accent-bar"></div>
      <p class="slogan">THE NORVEK ADVISORS</p>
      <div class="corner-decoration" role="img" aria-label="Decorative pattern of scattered blue and green squares in the top right corner"></div>
    </section>
  </div>
</body>
</html>
```